Layout für Broschüre für chemiefreie Lösung, Kühlwasser aufzubereiten
Zielgruppe
VELTROMAX hat eine Technologie entwickelt, die in der Industrie eingesetzt wird um in geschlossenen und offenen Kühlkreisläufen ohne Biozide und Korrosion Inhibitoren das Kühlwasser aufzubereiten. Mit VELTROMAX haben die Unternehmen eine chemiefreie Lösungen gegen Biofouling, Korrosion und Kalk. Zielgruppe sind alle Unternehmen die etwas produzieren oder Klimaanlagen / Heizungssysteme betreiben. Es geht um zukunftsorientierte und vor allem nachhaltige Technologie ohne Einsatz von Chemie.
Aufgabenstellung
Wir suchen für die Broschüre ein neues Layout, dass geradlinig und klar strukturiert ist, vor allem modern. Die Broschüre sollte DIN A 4 - Format sein in der gewohnten Struktur Umschlagseite innen und außen und 8 - 10 Innenseiten. Im Layout sollte ein roter Faden zu erkennen sein, aber nicht jede Seite gleich aussehen. Die Anlagen sind nur beispielhaft vom bestehenden Material und sollten vom Layout keinesfalls eine Orientierung geben, denn das soll verändert werden. Die Anlagen sind für einen inhaltlichen Überblick.

```html
<!DOCTYPE html>
<html lang="de">
<head>
<meta charset="utf-8">
<title>VELTROMAX Broschüre – Layout</title>
<link href="https://fonts.googleapis.com/css2?family=Montserrat:wght@300;400;600;700&family=Source+Sans+3:wght@400;600;700&display=swap" rel="stylesheet">
<style>
:root{
  --blue:#00a7e1;
  --blue-box:#4dc0ee;
  --blue-light:#d5ebf8;
  --green:#8dc63f;
  --green-band:#c3d981;
  --navy:#0b2c42;
  --ink:#222;
  --frame:#3a3a3a;
  --label:#444;
}
*{margin:0;padding:0;box-sizing:border-box}
html,body{width:1200px;height:2571px;overflow:hidden;background:#fff}
body{position:relative;font-family:"Source Sans 3",sans-serif;color:var(--ink)}
.page{position:absolute;overflow:hidden;background:#fff}
.frame{position:absolute;border:1px solid var(--frame);pointer-events:none}
.abs{position:absolute}
.photo{position:absolute}
.page-label{position:absolute;font-family:"Montserrat",sans-serif;font-weight:300;font-size:19px;color:var(--label)}
.brand{position:absolute;display:flex;align-items:center;gap:8px;font-family:"Montserrat",sans-serif;font-weight:700;color:var(--blue);letter-spacing:-.5px}
.brand-dot{border-radius:50%;background:var(--green)}
.tagline{position:absolute;font-family:"Montserrat",sans-serif;font-weight:400;font-size:13.5px;letter-spacing:-.2px}
.tagline .b{color:var(--blue)} .tagline .g{color:var(--green)}
.headline{position:absolute;font-family:"Montserrat",sans-serif;font-weight:300;line-height:1}
.small{font-size:6.6px;line-height:1.38;color:#222;font-weight:600}
.small p+p{margin-top:8px}
.stat{position:absolute;top:828px;width:93px;height:164px;background:var(--blue-box);color:#fff;text-align:center;font-family:"Montserrat",sans-serif}
.stat svg{position:absolute;left:26px;top:14px}
.stat .num{position:absolute;left:0;right:0;font-size:17px;font-weight:600}
.stat .txt{position:absolute;left:0;right:0;font-size:12.5px;font-weight:300;line-height:1.45}
.use{position:absolute;width:68px;text-align:center}
.use .pic{width:68px;height:68px}
.use h4{margin-top:8px;font-size:6.3px;font-weight:700;color:#4a5a66;line-height:1.25;text-transform:uppercase}
.use p{margin-top:6px;font-size:6.1px;line-height:1.35;color:#333;font-weight:600}
.cols{position:absolute;display:flex;gap:11px;color:#fff;font-size:6.3px;line-height:1.4;font-weight:600}
.cols div{width:103px}
.cols p+p{margin-top:9px}
.contact{position:absolute;font-size:6.6px;line-height:1.65;color:var(--blue);font-weight:700}
</style>
</head>
<body>

<!-- Vorderseite -->
<section class="page" style="left:602px;top:57px;width:361px;height:511px">
  <div class="brand" style="left:58px;top:55px;font-size:36px"><span class="brand-dot" style="width:14px;height:14px"></span>VELTROMAX</div>
  <div class="photo" role="img" aria-label="Wassertropfen mit Erdkugel über einer offenen Hand, vor türkisblauer Wasseroberfläche" style="left:0;top:169px;width:361px;height:284px;background:radial-gradient(ellipse at 50% 35%,#f2fbfd 0%,#cdeef3 35%,#7fd0e0 65%,#2aa7c9 100%)"></div>
  <div class="tagline" style="left:26px;top:472px"><span class="b">NACHHALTIG.</span> <span class="g">EFFIZIENT.</span> <span class="b">ZUKUNFTSORIENTIERT</span></div>
</section>
<div class="frame" style="left:601px;top:57px;width:363px;height:512px"></div>
<div class="page-label" style="left:602px;top:596px">Vorderseite (1)</div>

<!-- Innenseiten 2–3 -->
<section class="page" style="left:240px;top:723px;width:722px;height:511px">
  <div class="photo" role="img" aria-label="Blick unter die Wasseroberfläche mit einfallendem Sonnenlicht" style="left:0;top:0;width:361px;height:199px;background:linear-gradient(180deg,#b9dbe6 0%,#4f97b4 35%,#1d5f84 70%,#0f4566 100%)"></div>
  <h2 class="headline" style="left:35px;top:228px;font-size:23px">
    <span style="color:var(--blue)">Chemiefreie<br>Wasserbehandlung –</span><br>
    <span style="color:var(--green)">die Lösung gegen Biofilm,<br>Korrosion und Kalk</span>
  </h2>
  <div class="abs small" style="left:110px;top:339px;width:208px">
    <p>Seit über 15 Jahren konzentrieren wir uns auf die Einsparung lebensnotwendiger Ressourcen wie Wasser und die nachhaltige Behandlung ohne Chemie. Mit der chemikalienfreien VELTROMAX Technologie geben wir u.a. der Industrie, mittelständischen Unternehmen, Hotels und Wohnungsbaugesellschaften die Lösung auf Biofilm, Kalk und Korrosion ohne Chemie.</p>
    <p>Jedes Unternehmen, das die VELTROMAX Technologie einsetzt, spart nicht nur Kosten für Biozide, Salz und Korrosionsinhibitoren, sondern gleichzeitig auch für Reparatur und Wartung – und zeigt seinen Mitarbeitern und Kunden sein echtes nachhaltiges Engagement für Ökologie und Ökonomie.</p>
  </div>
  <div class="abs" style="left:0;top:477px;width:361px;height:34px;background:var(--navy)"></div>

  <div class="abs" style="left:361px;top:0;width:361px;height:199px;background:var(--green-band)"></div>
  <div class="abs small" style="left:406px;top:33px;width:272px;text-align:center;color:#333">Unser erfahrenes Team und zuverlässige Partner unterstützen Sie, die Kühlkreisläufe in der Produktion, sowie die Wasser- und Heizungsanlagen ohne Chemie aufzubereiten. Wir sind der Partner an Ihrer Seite vom ersten Gespräch, bis zur Inbetriebnahme und Wartung.</div>
  <div class="photo" role="img" aria-label="Wasser wird in ein Glas gegossen, grüner unscharfer Hintergrund" style="left:395px;top:312px;width:293px;height:165px;background:linear-gradient(100deg,#e6ee8a 0%,#8ac43c 35%,#3d8a2a 65%,#9cc968 100%)"></div>
</section>
<div class="stat" style="left:635px">
  <svg width="42" height="36" viewBox="0 0 42 36" fill="none" stroke="#fff" stroke-width="3" stroke-linejoin="round"><path d="M3 10h8l7 4 6-4h7l8 0v12l-8 6-6-4-5 4-9-6H3z"/><path d="M18 14l7 6"/></svg>
  <div class="num" style="top:80px">15</div>
  <div class="txt" style="top:102px">Jahre<br>Erfahrung</div>
</div>
<div class="stat" style="left:735px">
  <svg width="42" height="42" viewBox="0 0 42 42" fill="none" stroke="#fff" stroke-width="3" stroke-linecap="round"><circle cx="21" cy="21" r="18"/><path d="M13 17q2.5-3 5 0M24 17q2.5-3 5 0"/><path d="M12 25q9 9 18 0"/></svg>
  <div class="num" style="top:77px">895</div>
  <div class="txt" style="top:99px">Installierte<br>Veltromax<br>Systeme</div>
</div>
<div class="stat" style="left:835px">
  <svg width="44" height="36" viewBox="0 0 44 36" fill="#fff"><circle cx="22" cy="8" r="7"/><circle cx="8" cy="12" r="5"/><circle cx="36" cy="12" r="5"/><path d="M10 34q0-14 12-14t12 14z"/><path d="M0 30q0-11 8-11 3 0 5 2-5 4-5 9z"/><path d="M44 30q0-11-8-11-3 0-5 2 5 4 5 9z"/></svg>
  <div class="num" style="top:83px">24</div>
  <div class="txt" style="top:105px">qualifizierte<br>Experten</div>
</div>
<div class="frame" style="left:239px;top:723px;width:724px;height:512px"></div>
<div class="abs" style="left:601px;top:723px;width:1px;height:511px;background:var(--frame)"></div>

<!-- Innenseiten 4–5 -->
<section class="page" style="left:240px;top:1317px;width:722px;height:510px">
  <h2 class="headline" style="left:35px;top:32px;font-size:22px;color:var(--green)">Einsatzgebiete</h2>
  <div class="abs" style="left:0;top:103px;width:361px;height:407px;background:var(--blue-light)"></div>

  <div class="abs" style="left:361px;top:0;width:361px;height:303px;background:var(--blue)"></div>
  <h2 class="headline" style="left:394px;top:32px;font-size:22px;color:#fff">Wirkungsweise</h2>
  <div class="cols" style="left:470px;top:104px">
    <div><p>Das Kühlwasser durchläuft ein Modul, das die Struktur der gelösten Mineralien verändert, ohne Zusatzstoffe.</p><p>Kalk bleibt in Schwebe und lagert sich nicht an. Biofilm findet keinen Halt, Korrosion wird deutlich gebremst.</p></div>
    <div><p>Die Anlage arbeitet wartungsarm und kann in bestehende Kreisläufe integriert werden.</p><p>Messwerte werden laufend erfasst, so bleibt die Wasserqualität jederzeit transparent für Ihr Team.</p></div>
  </div>
  <div class="photo" role="img" aria-label="Drei Wassergläser von trüb bis klar vor hellblauem Hintergrund" style="left:395px;top:277px;width:292px;height:197px;background:linear-gradient(180deg,#7fcbe6 0%,#b7e2f1 55%,#e9f5fa 100%)"></div>
</section>

<div class="use" style="left:274px;top:1447px"><div class="pic" role="img" aria-label="Industrieanlage mit Kühltürmen" style="background:linear-gradient(#9cc3e0,#6b8aa0)"></div><h4>Industrie</h4><p>VELTROMAX verhindert den Prozess der Ablagerungen von Mineralien im gesamten Prozesskreislauf.</p></div>
<div class="use" style="left:349px;top:1447px"><div class="pic" role="img" aria-label="Kunststoffproduktion mit Maschinenteilen" style="background:linear-gradient(#3f7fc4,#c9b98a)"></div><h4>Kunststoff<br>industrie</h4><p>Durch die VELTROMAX VX-Modul Systeme werden den steigenden Wasser- und Chemikalienpreisen Rechnung getragen.</p></div>
<div class="use" style="left:424px;top:1447px"><div class="pic" role="img" aria-label="Lebensmittelproduktion in heller Halle" style="background:linear-gradient(#dfeef5,#e3b45a)"></div><h4>Lebensmittel<br>industrie</h4><p>Vor allem in den Sommermonaten wird das Wachstum vom Biofouling in den Anlagen forciert.</p></div>
<div class="use" style="left:499px;top:1447px"><div class="pic" role="img" aria-label="Grüne Pflanzen im Gewächshaus" style="background:linear-gradient(#c9e6c0,#3f8a2c)"></div><h4>Pflanzen- und<br>Tierzucht</h4><p>Landwirtschaft und Wasserwirtschaft müssen keine Gegensätze sein.</p></div>

<div class="use" style="left:274px;top:1632px"><div class="pic" role="img" aria-label="Operationsleuchte in einer Klinik" style="background:linear-gradient(#8fb7d6,#4d79a4)"></div><h4>Kliniken</h4><p>Jährlich werden in Kliniken unvorstellbar große Mengen an chemischen Mitteln verwendet.</p></div>
<div class="use" style="left:349px;top:1632px"><div class="pic" role="img" aria-label="Hotelhochhäuser an der Küste" style="background:linear-gradient(#4b8ed0,#a9c7df)"></div><h4>Hotels</h4><p>Der Sanitär- und Küchenbereich, Heizungs- und Wasserinstallationen im Hotel- und Gastronomie Gewerbe werden besonders stark beansprucht.</p></div>
<div class="use" style="left:424px;top:1632px"><div class="pic" role="img" aria-label="Moderner Wohnblock" style="background:linear-gradient(#eef3f6,#9aa7ad)"></div><h4>Wohnungsbau</h4><p>Verlängert die Lebensdauer von Trinkwassersystemen sowie Heiz- und Kühlanlagen in großen Wohnanlagen.</p></div>
<div class="use" style="left:499px;top:1632px"><div class="pic" role="img" aria-label="Modernes Einfamilienhaus" style="background:linear-gradient(#7fb6e3,#d8dcd8)"></div><h4>Eigenheim</h4><p>Veltromax verlängert die Lebensdauer von Trinkwassersystemen sowie Heiz- und Kühlanlagen im Eigenheim.</p></div>

<div class="frame" style="left:239px;top:1317px;width:724px;height:511px"></div>
<div class="abs" style="left:601px;top:1317px;width:1px;height:510px;background:var(--frame)"></div>

<!-- Rückseite -->
<section class="page" style="left:240px;top:1935px;width:360px;height:510px">
  <div class="brand" style="left:47px;top:80px;font-size:19px;gap:5px"><span class="brand-dot" style="width:8px;height:8px"></span>VELTROMAX</div>
  <div class="contact" style="left:232px;top:52px">
    VELTROMAX GmbH<br>Marion Albrecht-Kessler<br>Lindenweg 12<br>91099 Talheim<br>Tel.: 0123 – 456 7890<br>E-Mail: info@veltromax-beispiel.de<br>www.veltromax-beispiel.de
  </div>
  <div class="photo" role="img" aria-label="Wassertropfen mit Erdkugel über einer offenen Hand, vor türkisblauer Wasseroberfläche" style="left:0;top:168px;width:360px;height:284px;background:radial-gradient(ellipse at 50% 35%,#f2fbfd 0%,#cdeef3 35%,#7fd0e0 65%,#2aa7c9 100%)"></div>
</section>
<div class="frame" style="left:239px;top:1935px;width:362px;height:511px"></div>
<div class="page-label" style="left:239px;top:2473px">Rückseite (12)</div>

</body>
</html>
```